Construction material supplies company business card ****

1. Full company name “Marlow Aggregate Products Ltd”
I am after a Business card design for the company as a whole. We are better known in Solomon Islands as “Marlow Aggregate” for short.

We are a building materials supplier of
Ready Mixed Concrete, Bricks and Blocks,
Quarry products- gravel, aggregates, sand etc.
Cement distributor/retailer of reputable brands.
Other prefab concrete products. Culverts, wave breakers, concrete retaining blocks etc.

2. Competitive Advantage over Competition: Quality, efficient, professional, dependable, reliable

3. We want people to feel trust worthy, high quality, strong when they see our brand

5. No preference to color. Maybe more sturdy and corporate. Not fancy.

Industry/Entity Type

CONSTRUCTION SUPPLY

Contact Information for Business Card

Name, Position, office phone mob phone, email

Requirements
Must have
• the company logo
Nice to have
• would like to see a mixture of designs, of with logo only and also with simple graphic designs to bring out the company whilst still have the strong sturdy professional feeling

```html
<!DOCTYPE html>
<html lang="en">
<head>
<meta charset="utf-8">
<title>Marlow Aggregate – Business Card</title>
<link rel="stylesheet" href="https://fonts.googleapis.com/css2?family=Oswald:wght@500&family=Lato:wght@400&family=Exo+2:wght@600&display=swap">
<style>
  :root {
    --backdrop: #2f3033;
    --card-blue: #1a4d79;
    --card-blue-deep: #123a5e;
    --silver: #dfe3e8;
    --silver-soft: #c3cad2;
    --divider: rgba(223, 227, 232, 0.55);
  }
  * { margin: 0; padding: 0; box-sizing: border-box; }
  html, body {
    width: 1200px;
    height: 900px;
    overflow: hidden;
    background: var(--backdrop);
  }
  .canvas {
    width: 1200px;
    height: 900px;
    display: flex;
    flex-direction: column;
    align-items: center;
    justify-content: center;
    gap: 48px;
  }
  .card {
    width: 630px;
    height: 360px;
    border-radius: 4px;
    background: radial-gradient(ellipse at 40% 35%, var(--card-blue) 0%, var(--card-blue-deep) 100%);
    box-shadow: 0 14px 30px rgba(0, 0, 0, 0.45);
    position: relative;
    overflow: hidden;
  }
  .card--front {
    display: flex;
    align-items: center;
    justify-content: center;
  }
  .brand {
    display: flex;
    align-items: center;
    gap: 18px;
  }
  .brand-mark {
    width: 30px;
    height: 30px;
    background: var(--silver);
    flex: none;
  }
  .brand-name {
    font-family: "Exo 2", sans-serif;
    font-weight: 600;
    font-size: 38px;
    letter-spacing: 3px;
    text-transform: uppercase;
    color: var(--silver);
    line-height: 1;
  }
  .card--back {
    display: flex;
    align-items: center;
    justify-content: center;
    gap: 28px;
  }
  .identity {
    text-align: right;
  }
  .person-name {
    font-family: "Oswald", sans-serif;
    font-weight: 500;
    font-size: 34px;
    letter-spacing: 1px;
    text-transform: uppercase;
    color: var(--silver);
    line-height: 1.1;
  }
  .person-role {
    font-family: "Lato", sans-serif;
    font-size: 16px;
    color: var(--silver-soft);
    margin-top: 4px;
  }
  .divider {
    width: 1px;
    height: 120px;
    background: var(--divider);
  }
  .contact-list {
    list-style: none;
    font-family: "Lato", sans-serif;
    font-size: 17px;
    color: var(--silver);
    line-height: 1.6;
  }
  .contact-list li {
    display: flex;
    align-items: center;
    gap: 8px;
    white-space: nowrap;
  }
  .contact-label {
    color: var(--silver-soft);
    width: 14px;
  }
  .contact-icon {
    width: 13px;
    height: 13px;
    flex: none;
  }
</style>
</head>
<body>
  <main class="canvas">
    <section class="card card--front" aria-label="Card front">
      <div class="brand">
        <span class="brand-mark" aria-hidden="true"></span>
        <span class="brand-name">Marlow Aggregate</span>
      </div>
    </section>

    <section class="card card--back" aria-label="Card back">
      <div class="identity">
        <p class="person-name">Daniel Harper</p>
        <p class="person-role">President</p>
      </div>
      <span class="divider"></span>
      <ul class="contact-list">
        <li>
          <svg class="contact-icon" viewBox="0 0 16 16" aria-hidden="true">
            <path d="M4 1.5 6.2 4.2 5 6c.8 1.8 2.2 3.2 4 4l1.8-1.2 2.7 2.2-1.2 2.4C8 13 3 8 1.6 2.7Z" fill="var(--silver)"/>
          </svg>
          <span class="contact-label">O</span>555-014-2837
        </li>
        <li>
          <svg class="contact-icon" viewBox="0 0 16 16" aria-hidden="true">
            <rect x="4" y="1" width="8" height="14" rx="1.5" fill="none" stroke="var(--silver)" stroke-width="1.4"/>
            <circle cx="8" cy="12.3" r="0.9" fill="var(--silver)"/>
          </svg>
          <span class="contact-label">M</span>555-014-2851
        </li>
        <li>
          <svg class="contact-icon" viewBox="0 0 16 16" aria-hidden="true">
            <rect x="1.5" y="3.5" width="13" height="9" fill="none" stroke="var(--silver)" stroke-width="1.4"/>
            <path d="M1.5 3.5 8 9l6.5-5.5" fill="none" stroke="var(--silver)" stroke-width="1.4"/>
          </svg>
          info@marlowaggregate.com
        </li>
        <li>
          <svg class="contact-icon" viewBox="0 0 16 16" aria-hidden="true">
            <circle cx="8" cy="8" r="6.3" fill="none" stroke="var(--silver)" stroke-width="1.3"/>
            <ellipse cx="8" cy="8" rx="2.6" ry="6.3" fill="none" stroke="var(--silver)" stroke-width="1.1"/>
            <path d="M1.7 8h12.6" stroke="var(--silver)" stroke-width="1.1"/>
          </svg>
          www.marlowaggregate.com
        </li>
      </ul>
    </section>
  </main>
</body>
</html>
```